Harlow Crest Holdings (Remodeling company) needs a logo and business card

We need a business card design for a new company. We "flip" upmarket houses (buy, remodel and sell) in the Austin, TX area. I'd like neutral colors (grey, white, gold black). I would like it to include a simple, clean logo. Our designs are modern and uncluttered and I would like that reflected in the business card design.

Target Market(s)

Young professionals, Families, Retirees. Our properties will sell for $750k+

Industry/Entity Type

Real Estate

Contact Information for Business Card

Harlow Crets Holdings
Mona Harlow
(979) 555 0142
Owner
Rolf Tandem
(512) 555 0176
Realtor

Logo Text

Harlow Crest Holdings

Font styles to use
Serif
Script

Requirements
Must have
• Simple, classic design
Nice to have
• Clean lines, modern look
Should not have
• Too traditionally

```html
<!DOCTYPE html>
<html lang="en">
<head>
<meta charset="UTF-8">
<title>Harlow Crest Holdings — Business Card</title>
<link href="https://fonts.googleapis.com/css2?family=Michroma&family=Roboto+Condensed:wght@400&display=swap" rel="stylesheet">
<style>
  :root {
    --backdrop: #a9a7a8;
    --card-black: #0c0c0c;
    --card-white: #f7f6f4;
    --gold: #d4a02f;
    --ink: #1c1c1c;
    --ink-soft: #4a4a4a;
    --rule: #d9d7d3;
  }
  html, body {
    margin: 0;
    width: 1200px;
    height: 1200px;
    overflow: hidden;
    background: var(--backdrop);
  }
  .canvas {
    position: relative;
    width: 1200px;
    height: 1200px;
  }
  .card {
    position: absolute;
    width: 712px;
    height: 418px;
    border-radius: 22px;
    overflow: hidden;
  }
  .card--front {
    left: 238px;
    top: 118px;
    background: var(--card-black);
  }
  .card--back {
    left: 230px;
    top: 644px;
    background: var(--card-white);
  }
  .interior-photo {
    position: absolute;
    inset: 0;
  }
  .card--front .interior-photo {
    background: radial-gradient(ellipse at 60% 55%, #1d1c1a 0%, #111111 55%, #0a0a0a 100%);
  }
  .card--back .interior-photo {
    background: linear-gradient(180deg, #fbfaf8 0%, #efedea 60%, #f4f3f0 100%);
  }
  .wordmark {
    position: absolute;
    font-family: "Michroma", sans-serif;
    text-align: center;
    letter-spacing: 0.5px;
    margin: 0;
  }
  .card--front .wordmark {
    left: 0;
    right: 0;
    top: 205px;
    font-size: 30px;
    color: #ffffff;
  }
  .card--back .wordmark {
    left: 30px;
    width: 345px;
    top: 150px;
    font-size: 25px;
    line-height: 1.45;
    color: var(--ink);
  }
  .divider {
    position: absolute;
    left: 393px;
    top: 100px;
    width: 1px;
    height: 160px;
    background: var(--rule);
  }
  .contact {
    position: absolute;
    left: 421px;
    top: 126px;
  }
  .contact__name {
    font-family: "Michroma", sans-serif;
    font-size: 22px;
    font-weight: 400;
    color: var(--ink);
    margin: 0;
  }
  .contact__role {
    font-family: "Roboto Condensed", sans-serif;
    font-size: 16px;
    color: var(--ink-soft);
    margin: 6px 0 0;
  }
  .contact__list {
    list-style: none;
    padding: 0;
    margin: 22px 0 0;
    font-family: "Roboto Condensed", sans-serif;
    font-size: 17px;
    color: var(--ink);
  }
  .contact__list li {
    display: flex;
    align-items: center;
    gap: 16px;
    height: 29px;
  }
  .contact__list svg { width: 19px; height: 16px; flex: none; }
  .band-black {
    position: absolute;
    left: 0;
    right: 0;
    bottom: 0;
    height: 26px;
    background: var(--card-black);
  }
  .band-gold {
    position: absolute;
    left: 360px;
    right: 0;
    bottom: 0;
    height: 52px;
    background: var(--gold);
    clip-path: polygon(30px 0, 100% 0, 100% 100%, 0 100%);
  }
  .website {
    position: absolute;
    left: 421px;
    bottom: 16px;
    margin: 0;
    font-family: "Roboto Condensed", sans-serif;
    font-size: 16px;
    color: var(--ink);
  }
</style>
</head>
<body>
<div class="canvas">
  <section class="card card--front">
    <div class="interior-photo" role="img" aria-label="Dim photograph of a modern living room interior"></div>
    <p class="wordmark">Harlow Crest Holdings</p>
  </section>

  <section class="card card--back">
    <div class="interior-photo" role="img" aria-label="Faded photograph of a bright, white modern living room interior"></div>
    <p class="wordmark">Harlow Crest<br>Holdings</p>
    <div class="divider"></div>
    <div class="contact">
      <h1 class="contact__name">Mona Harlow</h1>
      <p class="contact__role">Owner</p>
      <ul class="contact__list">
        <li>
          <svg viewBox="0 0 19 16" aria-hidden="true"><path fill="#d4a02f" d="M1 5c0-3 4-4 8.5-4S18 2 18 5l-3 1-1-2H5L4 6 1 5zM4 8h11l2 7H2z"/><circle cx="9.5" cy="11" r="2" fill="#f7f6f4"/></svg>
          <span>(979) 555 0142</span>
        </li>
        <li>
          <svg viewBox="0 0 19 16" aria-hidden="true"><rect x="1" y="2" width="17" height="12" fill="#d4a02f"/><path d="M1 2l8.5 7L18 2" fill="none" stroke="#f7f6f4" stroke-width="1.5"/></svg>
          <span>mona@harlowcrestholdings.com</span>
        </li>
      </ul>
    </div>
    <div class="band-black"></div>
    <div class="band-gold"></div>
    <p class="website">www.harlowcrestholdings.com</p>
  </section>
</div>
</body>
</html>
```